Creating a Label for a new CBD Vape Line call "Brizel".

This will be a project that will create the first label design on a BRIZEL Vape product that is being rolled out in Colorado. The vape line will cater to high concentration CBD Vape sold in disposable vape pens and replacement cartridge's. In the sea of vape pens we want our packaging to stand out with a bold, bright, clean, abstract design that will highlight the brand "BRIZEL" in a font that stands out and is quickly recognized. The target demographic for this line is 18-29 years of age. The mock up of the brizel vape picture does not meet our marketing desire, I just wanted to show you the approximate shape and size of the label and that the font used for the label will be added to the actual pen. This pen will have 100% CBD, cut with all natural terpenes with no need for chemicals like PG or VG, not many on the market like that. I included several marketing logos that caught our eye with other type product, please look at those as examples but we are open to creativity.

Target Market(s)

18-29 year old

Industry/Entity Type

CBD and Vape

Font styles to use
Serif
Sans Serif

Requirements
Must have
• bold, colorful, fun, eye catching
Nice to have
• Several brand ideas presented to give the flavor of the marketing. The example font on the prototype is not 'cool enough' to use, we'd like that name BRIZEL to look and feel brizzzel. :-)
Should not have
• old school, boring, dull colors, small font

```html
<!DOCTYPE html>
<html lang="en">
<head>
<meta charset="utf-8">
<title>Brizel Velta Vape Label</title>
<link rel="stylesheet" href="https://fonts.googleapis.com/css2?family=Michroma&family=Questrial&family=Montserrat:wght@500;700&display=swap">
<style>
  :root {
    --backdrop: #8c8c8c;
    --label: #ffffff;
    --ink: #3a3a3a;
    --ink-strong: #2e2e2e;
    --pattern-tone: #f1f1f1;
    --grad-orange: #f0a530;
    --grad-green: #3a9a5e;
    --grad-magenta: #9a3290;
    --grad-blue: #1f5aa0;
  }
  * { box-sizing: border-box; margin: 0; padding: 0; }
  html, body { width: 1200px; height: 960px; overflow: hidden; }
  body {
    background: var(--backdrop);
    position: relative;
    font-family: "Questrial", sans-serif;
    color: var(--ink);
  }
  .label {
    position: absolute;
    left: 475px;
    top: 30px;
    width: 250px;
    height: 900px;
    background: var(--label);
    overflow: hidden;
  }
  .texture-zone {
    position: absolute;
    left: 0; right: 0; bottom: 0;
    height: 384px;
    background: linear-gradient(to bottom, var(--label), var(--pattern-tone) 30%);
  }
  .brand {
    position: absolute;
    top: 44px; left: 0; right: 0;
    display: flex;
    flex-direction: column;
    align-items: center;
  }
  .brand-dot {
    width: 80px; height: 80px;
    border-radius: 50%;
    background: var(--ink);
  }
  .brand-name {
    margin-top: 14px;
    font-family: "Questrial", sans-serif;
    font-size: 27px;
    letter-spacing: 4px;
    color: var(--ink);
  }
  .hero-art {
    position: absolute;
    left: 14px;
    top: 224px;
    width: 200px;
    height: 448px;
    border-radius: 6px;
    background: linear-gradient(200deg, var(--grad-orange) 0%, var(--grad-green) 32%, var(--grad-magenta) 72%, var(--grad-blue) 100%);
  }
  .product-info {
    position: absolute;
    top: 686px; left: 0; right: 0;
    display: flex;
    flex-direction: column;
    align-items: center;
    text-align: center;
  }
  .product-line {
    font-family: "Michroma", sans-serif;
    font-size: 14px;
    letter-spacing: 2px;
    color: var(--ink-strong);
  }
  .strength-pill {
    margin-top: 10px;
    padding: 5px 14px;
    border-radius: 16px;
    background: var(--ink-strong);
    color: var(--label);
    font-family: "Montserrat", sans-serif;
    font-weight: 700;
    font-size: 15px;
    letter-spacing: 1.5px;
  }
  .format {
    margin-top: 10px;
    font-family: "Montserrat", sans-serif;
    font-weight: 500;
    font-size: 14px;
    letter-spacing: 1.5px;
    color: var(--ink-strong);
  }
  .claims {
    position: absolute;
    top: 806px; left: 0; right: 0;
    text-align: center;
    font-size: 18px;
    line-height: 40px;
    color: var(--ink);
  }
</style>
</head>
<body>
  <main class="label">
    <div class="texture-zone" role="img" aria-label="Light hexagon texture panel"></div>
    <header class="brand">
      <span class="brand-dot"></span>
      <span class="brand-name">BRIZEL</span>
    </header>
    <div class="hero-art" role="img" aria-label="Abstract flowing ribbon artwork in orange, green, magenta and blue"></div>
    <section class="product-info">
      <p class="product-line">VELTA VAPE</p>
      <p class="strength-pill">300MG CBD</p>
      <p class="format">DISPOSABLE PEN</p>
    </section>
    <section class="claims">
      <p>100% CBD</p>
      <p>All natural terpenes</p>
    </section>
  </main>
</body>
</html>
```